Business Card Design Project

We are looking to redesign the logo, business card and stationary of one of our group companies - KESTRAL SUPPLY COMPANY LLC.

The company specialises in industrial PVC and CPVC Piping systems. It is situated in the Middle East and the focus is purely in this region.

The logo work is already completed. The file is uploaded for the reference.

We are looking for a clean minimalistic design for the business card.

regards
Dorun

Hello Everyone!

Thanks for submitting your designs. 

Yet to find the right design. Probably the below links will give you guys some more idea on what we would like.

Minimalist design with some creativity.

Dorun

http://pixelorchard-example.com/inspiration/15-beautifully-minimal-business-cards

http://www.graphvane-example.com/2011/11/14/30-minimalist-business-card-design/

http://www.topdrafthub-example.com/inspiration/minimal-business-cards/

Target Market(s)

Industrial users

Industry/Entity Type

Industrial

Requirements
Must have
• - Minimalistic design

- Back side of the card should include the manufacturer PLUMARC CANADA's decal. The file is upload for the reference

- Further information
Company Name:
KESTRAL SUPPLY COMPANY LLC
Address:
PO Box 3857, Sharjah Industrial Area 5, Tarvesh Road
Sharjah, United Arab Emirates
Telephone:
+971-6-5000-912
Fax:
+977-6-5000-913
Email:
mail@ksqholdings.com

- FYI, Kestral Supply Company LLC is the authorised distributor for PLUMARC CANADA in the UAE. For further information on plumarc please visit the website www.plumarc.ca

```html
<!DOCTYPE html>
<html lang="en">
<head>
<meta charset="utf-8">
<title>Kestral Supply Company LLC – Business Card</title>
<link rel="stylesheet" href="https://fonts.googleapis.com/css2?family=Open+Sans:wght@600;700&family=Barlow+Semi+Condensed:wght@600&display=swap">
<style>
  :root {
    --page-bg: #ececec;
    --card-bg: #ffffff;
    --ink: #333333;
    --brand-blue: #3f68b4;
    --brand-blue-light: #7aaee0;
    --brand-blue-dark: #3658a8;
    --label-blue: #3d62a6;
    --card-edge: #d6d6d6;
  }
  * { margin: 0; padding: 0; box-sizing: border-box; }
  html, body {
    width: 1200px;
    height: 1124px;
    overflow: hidden;
    background: var(--page-bg);
  }
  .canvas {
    position: relative;
    width: 1200px;
    height: 1124px;
  }
  .card {
    position: absolute;
    top: 128px;
    width: 550px;
    height: 868px;
    background: var(--card-bg);
    border: 1px solid var(--card-edge);
    overflow: hidden;
  }
  .card--front {
    left: 30px;
    border-top-right-radius: 175px;
  }
  .card--back {
    left: 620px;
    border-top-left-radius: 175px;
  }

  /* Front */
  .brand-mark {
    position: absolute;
    left: 195px;
    top: 150px;
    width: 160px;
    height: 160px;
    background: var(--brand-blue);
  }
  .brand-name {
    position: absolute;
    left: 0;
    right: 0;
    top: 440px;
    text-align: center;
    font-family: "Open Sans", sans-serif;
    font-weight: 700;
    font-size: 96px;
    line-height: 1;
    letter-spacing: -2px;
    color: var(--ink);
  }
  .company-band {
    position: absolute;
    left: 0;
    right: 0;
    top: 642px;
    height: 107px;
    background: linear-gradient(to bottom, var(--brand-blue-light), var(--brand-blue-dark));
    display: flex;
    align-items: center;
    justify-content: flex-end;
    padding-right: 40px;
  }
  .company-band__text {
    font-family: "Barlow Semi Condensed", sans-serif;
    font-weight: 600;
    font-size: 38px;
    color: #ffffff;
    letter-spacing: 0.5px;
  }

  /* Back */
  .contact {
    position: absolute;
    left: 0;
    right: 0;
    text-align: center;
    font-family: "Open Sans", sans-serif;
    font-weight: 600;
    color: var(--ink);
    font-size: 27px;
    line-height: 1.32;
  }
  .contact--address { top: 120px; }
  .contact--city { top: 300px; }
  .contact__label {
    display: block;
    color: var(--label-blue);
    font-weight: 700;
  }
  .contact--phone { top: 460px; }
  .contact--fax { top: 562px; }
  .contact--email { top: 664px; }
  .tab {
    position: absolute;
    width: 90px;
    height: 104px;
    background: linear-gradient(to bottom, var(--brand-blue-light), var(--brand-blue-dark));
  }
  .tab--left {
    left: 0;
    top: 612px;
    border-radius: 0 52px 52px 0;
  }
  .tab--right {
    right: 0;
    top: 668px;
    border-radius: 52px 0 0 52px;
  }
</style>
</head>
<body>
<main class="canvas">
  <section class="card card--front" aria-label="Business card front">
    <div class="brand-mark"></div>
    <div class="brand-name">kestral</div>
    <div class="company-band">
      <span class="company-band__text">SUPPLY COMPANY LLC</span>
    </div>
  </section>

  <section class="card card--back" aria-label="Business card back">
    <p class="contact contact--address">PO Box 3857<br>Sharjah Industrial Area 5<br>Tarvesh Road</p>
    <p class="contact contact--city">Sharjah, United Arab<br>Emirates</p>
    <p class="contact contact--phone"><span class="contact__label">Telephone:</span>+971-6-5000-912</p>
    <p class="contact contact--fax"><span class="contact__label">Fax:</span>+977-6-5000-913</p>
    <p class="contact contact--email"><span class="contact__label">Email:</span>mail@ksqholdings.com</p>
    <div class="tab tab--left"></div>
    <div class="tab tab--right"></div>
  </section>
</main>
</body>
</html>
```